Fatigued and Overloaded by COVID Messages? We need original illustrations to show that.

Everywhere you look there are messages about COVID. That is leading many people to feel fatigued and overloaded by the messages.

We surveyed U.S. adults March 20th - 24th, 2020 and measured message fatigue, information overload, perceived repetition, and perceived exaggeration. Here is how participants responded:

When it comes to coronavirus . . .
55% feel exhausted by all the messages.
54% feel overloaded by the amount of information.
51% feel that the messages are repetitive.
47% feel like messages exaggerate how bad it is.

In other words, almost half of U.S. adults show signs of message fatigue, information overload, perceived message repetition, and perceived message exaggeration.

We will continue to survey 400 adults every week for the next 16 weeks. Each time we will measure message fatigue, information overload, perceived repetition, and perceived exaggeration. We expect that it will increase over time.

What are we looking for? We need innovative and original illustrations that attempt to communicate these findings. The illustrations would visualize message fatigue, information overload, perceived message repetition, and perceived message exaggeration.

What sort of visual are we looking for? Our preference is for an original illustration (or set of illustrations). Our preference is for creative and powerful illustrations, but we are also open to the creative and well-executed infographics.

We need these images fast . We will award monetary prizes to the 3 best designs. If we like more than that, then we might purchase more (e.g., in past contests, we have purchased as many as 30 designs).

What we will need:
(1) The illustrations must be original and we will need the photoshop and/or illustrator files for all artwork. (By original, we mean that the illustrations are 100% created by you. Our organization requires that we utilize only original illustrated work. We have had issues with free imagery being pirated and reposted as free. We sidestep that issue by just having everything created.)

(2) The illustration should say, somewhere: "Based on a survey of 400 U.S. adults conducted March 20 - 24th, 2020."

(3) We will have almost 4 months worth of data by the time this is done. In other words, the illustrations might be able to help us present that weekly data.

(4) We have conducted other Artvendo projects. It might be helpful to examine designs we liked in the past. For example, here is another COVID project we just finished:

https://jobs.artvendo-example.com/job/5162048

Target Market(s)

U.S. adults

Requirements
Must have
• Original illustrations. Mobile friendly design. People will view this on their smartphones.
Nice to have
• A design that we can use to communicate the data across time.

```html
<!DOCTYPE html>
<html lang="en">
<head>
<meta charset="utf-8">
<title>Coronavirus Message Fatigue</title>
<link href="https://fonts.googleapis.com/css2?family=Anton&family=Oswald:wght@600;700&family=Work+Sans:wght@400;500&display=swap" rel="stylesheet">
<style>
  :root {
    --teal: #64adbd;
    --teal-dark: #4f97a8;
    --indigo: #4b52a8;
    --lavender: #a9acdb;
    --track: #e6e7e9;
    --dash: #8e8fc6;
    --ink: #5a5a5a;
    --paper: #ffffff;
  }
  * { box-sizing: border-box; margin: 0; padding: 0; }
  html, body { width: 830px; height: 1200px; overflow: hidden; background: var(--paper); }
  .poster { position: relative; width: 830px; height: 1200px; background: var(--paper); }
  .frame { position: absolute; left: 22px; top: 26px; width: 790px; height: 1146px; border: 3px solid var(--teal); }

  .source {
    position: absolute; top: 66px; left: 0; width: 830px; text-align: center;
    font: 400 17px/1 "Work Sans", sans-serif; color: var(--ink);
  }
  .title {
    position: absolute; top: 96px; left: 0; width: 830px;
    display: flex; justify-content: center; align-items: center;
    font: 400 108px/1 "Anton", sans-serif; color: var(--teal); letter-spacing: 1px;
  }
  .title .virus-o { width: 74px; height: 92px; margin: 0 2px; }
  .headline {
    position: absolute; top: 194px; left: 0; width: 830px; text-align: center;
    font: 700 34px/42px "Oswald", sans-serif; color: var(--indigo); letter-spacing: 0.2px;
  }

  .illustration {
    position: absolute; left: 232px; top: 352px; width: 494px; height: 536px;
    background: radial-gradient(ellipse at 50% 45%, #c9cbea 0%, #dfe0f3 55%, #f7f7fc 100%);
    border-radius: 40px;
  }

  .bar { position: absolute; width: 20px; background: var(--track); border-radius: 10px 10px 0 0; overflow: hidden; }
  .bar .fill { position: absolute; left: 0; bottom: 0; width: 100%; background: var(--teal); }

  .stat { position: absolute; }
  .stat .value { font: 600 34px/1 "Oswald", sans-serif; color: var(--teal); }
  .stat .label { font: 400 20px/22px "Work Sans", sans-serif; color: var(--indigo); margin-top: 8px; }
  .stat.right { text-align: right; }
  .icon { position: absolute; }

  .divider { position: absolute; left: 84px; top: 950px; width: 650px; border-top: 3px dashed var(--dash); }

  .summary {
    position: absolute; top: 978px; left: 0; width: 830px; text-align: center;
    font: 600 27px/34px "Oswald", sans-serif; color: var(--teal);
  }
</style>
</head>
<body>
<main class="poster">
  <div class="frame"></div>

  <p class="source">Based on a survey of 400 U.S. adults conducted March 20 - 24th, 2020.</p>

  <h1 class="title" aria-label="Coronavirus">
    <span>COR</span>
    <svg class="virus-o" viewBox="0 0 74 92" aria-hidden="true">
      <g stroke="var(--teal-dark)" stroke-width="3" stroke-linecap="round">
        <line x1="37" y1="46" x2="37" y2="8"/><line x1="37" y1="46" x2="37" y2="84"/>
        <line x1="37" y1="46" x2="2" y2="46"/><line x1="37" y1="46" x2="72" y2="46"/>
        <line x1="37" y1="46" x2="12" y2="20"/><line x1="37" y1="46" x2="62" y2="72"/>
        <line x1="37" y1="46" x2="62" y2="20"/><line x1="37" y1="46" x2="12" y2="72"/>
      </g>
      <circle cx="37" cy="46" r="28" fill="var(--teal)"/>
    </svg>
    <span>NAVIRUS</span>
  </h1>

  <h2 class="headline">IS LEADING MANY PEOPLE TO FEEL<br>FATIGUED AND OVERLOADED</h2>

  <div class="illustration" role="img" aria-label="Illustration of four tired people overwhelmed by coronavirus messages, some wearing masks, holding their heads"></div>

  <!-- exhausted -->
  <svg class="icon" style="left:99px;top:354px" width="98" height="108" viewBox="0 0 98 108" aria-hidden="true">
    <rect x="0" y="10" width="26" height="58" fill="var(--indigo)"/>
    <rect x="72" y="10" width="26" height="58" fill="var(--indigo)"/>
    <rect x="24" y="0" width="50" height="66" fill="var(--indigo)"/>
    <g stroke="#fff" stroke-width="2.5">
      <line x1="30" y1="10" x2="68" y2="10"/><line x1="30" y1="20" x2="68" y2="20"/>
      <line x1="30" y1="30" x2="68" y2="30"/><line x1="30" y1="40" x2="68" y2="40"/>
      <line x1="30" y1="50" x2="68" y2="50"/>
    </g>
    <circle cx="48" cy="68" r="5" fill="var(--teal)"/>
    <path d="M43 74 Q36 86 36 106" stroke="var(--teal)" stroke-width="4" fill="none" stroke-linecap="round"/>
  </svg>
  <div class="bar" style="left:60px;top:386px;height:191px"><div class="fill" style="height:105px"></div></div>
  <div class="stat" style="left:93px;top:472px">
    <div class="value">55%</div>
    <div class="label">feel exhausted<br>by all the<br>messages.</div>
  </div>

  <!-- repetitive -->
  <svg class="icon" style="left:626px;top:282px" width="94" height="92" viewBox="0 0 94 92" aria-hidden="true">
    <path d="M20 74 A42 42 0 1 1 48 88" stroke="var(--indigo)" stroke-width="5" fill="none" stroke-linecap="round"/>
    <path d="M8 66 L20 80 L26 62" stroke="var(--indigo)" stroke-width="5" fill="none" stroke-linecap="round" stroke-linejoin="round"/>
    <circle cx="47" cy="46" r="16" fill="var(--teal)"/>
    <g stroke="#fff" stroke-width="2.5"><line x1="39" y1="40" x2="55" y2="40"/><line x1="38" y1="46" x2="56" y2="46"/><line x1="39" y1="52" x2="55" y2="52"/></g>
  </svg>
  <div class="bar" style="left:733px;top:266px;height:193px"><div class="fill" style="height:96px"></div></div>
  <div class="stat right" style="right:102px;top:384px">
    <div class="value">51%</div>
    <div class="label">feel that the messages<br>are repetitive.</div>
  </div>

  <!-- exaggerate -->
  <svg class="icon" style="left:107px;top:728px" width="82" height="78" viewBox="0 0 82 78" aria-hidden="true">
    <circle cx="41" cy="39" r="20" fill="var(--teal)"/>
    <g stroke="#fff" stroke-width="2.5"><line x1="32" y1="32" x2="50" y2="32"/><line x1="30" y1="39" x2="52" y2="39"/><line x1="32" y1="46" x2="50" y2="46"/></g>
    <g stroke="var(--indigo)" stroke-width="5" fill="none" stroke-linecap="round" stroke-linejoin="round">
      <path d="M4 14 L4 4 L14 4"/><path d="M68 4 L78 4 L78 14"/>
      <path d="M4 64 L4 74 L14 74"/><path d="M68 74 L78 74 L78 64"/>
    </g>
  </svg>
  <div class="bar" style="left:65px;top:712px;height:191px"><div class="fill" style="height:89px"></div></div>
  <div class="stat" style="left:98px;top:820px">
    <div class="value">47%</div>
    <div class="label">feel like messages<br>exaggerate how bad it is.</div>
  </div>

  <!-- overloaded -->
  <svg class="icon" style="left:603px;top:692px" width="120" height="86" viewBox="0 0 120 86" aria-hidden="true">
    <line x1="16" y1="82" x2="110" y2="40" stroke="var(--indigo)" stroke-width="6" stroke-linecap="round"/>
    <path d="M62 60 L76 82 L48 82 Z" fill="var(--indigo)"/>
    <circle cx="26" cy="48" r="20" fill="var(--teal)"/>
    <rect x="23" y="44" width="6" height="14" fill="#fff"/><circle cx="26" cy="38" r="3" fill="#fff"/>
    <circle cx="112" cy="8" r="6" fill="var(--teal)"/>
    <path d="M108 18 L98 36 L112 36 L112 44" stroke="var(--teal)" stroke-width="6" fill="none" stroke-linecap="round" stroke-linejoin="round"/>
  </svg>
  <div class="bar" style="left:733px;top:700px;height:190px"><div class="fill" style="height:102px"></div></div>
  <div class="stat right" style="right:107px;top:791px">
    <div class="value">54%</div>
    <div class="label">feel overloaded<br>by the amount<br>of information.</div>
  </div>

  <div class="divider"></div>

  <p class="summary">In other words, almost half of U.S. adults<br>show signs of message fatigue, information<br>overload, perceived message repetition, and<br>perceived message exaggeration</p>
</main>
</body>
</html>
```